Talvick Industrial Maintenance Business Card

Design a business card with the following information, logo must be included.
Talvick Industrial Maintenance
Dan Pelfrey Jr.
Pone 555-214-7608
email dan.pelfrey.jr@mailvantor.com

```html
<!DOCTYPE html>
<html lang="en">
<head>
<meta charset="utf-8">
<title>Talvick Industrial Maintenance – Business Card</title>
<link href="https://fonts.googleapis.com/css2?family=Montserrat:wght@500;600;700&display=swap" rel="stylesheet">
<style>
  :root {
    --backdrop: #444446;
    --brand-blue: #1570b8;
    --brand-blue-deep: #0f5f9e;
    --paper: #f6f6f6;
    --paper-shade: #e6e6e6;
    --icon-grey: #6e6e6e;
    --white: #ffffff;
  }
  * { box-sizing: border-box; margin: 0; padding: 0; }
  html, body { width: 1200px; height: 1200px; overflow: hidden; }
  body {
    background: var(--backdrop);
    font-family: "Montserrat", sans-serif;
    position: relative;
  }
  .card {
    position: absolute;
    left: 233px;
    width: 734px;
    height: 448px;
    border-radius: 31px;
    overflow: hidden;
    box-shadow: 0 6px 14px rgba(0,0,0,0.45);
  }
  .card--front { top: 129px; background: var(--brand-blue); }
  .card--back { top: 623px; background: var(--paper); }

  .pattern-area {
    position: absolute;
    left: 0; top: 0;
    width: 420px; height: 100%;
  }
  .card--front .pattern-area {
    background: radial-gradient(circle at 30% 55%, var(--brand-blue-deep) 0%, var(--brand-blue) 70%);
  }
  .card--back .pattern-area {
    left: 300px; width: 434px;
    background: radial-gradient(circle at 55% 50%, var(--paper-shade) 0%, var(--paper) 70%);
  }

  .emblem-ring {
    position: absolute;
    left: 605px; top: 225px;
    width: 0; height: 0;
  }
  .emblem-ring::before {
    content: "";
    position: absolute;
    left: -200px; top: -200px;
    width: 400px; height: 400px;
    border-radius: 50%;
    border: 54px solid var(--white);
  }
  .card--back .emblem-ring { top: 234px; }
  .card--back .emblem-ring::before { border-color: var(--brand-blue); }

  .brand {
    position: absolute;
    display: flex;
    align-items: center;
    gap: 12px;
    font-weight: 600;
  }
  .brand__dot {
    width: 74px; height: 74px;
    border-radius: 50%;
    flex: none;
  }
  .brand__name { line-height: 1; }
  .brand__name .line-main { display: block; font-size: 40px; letter-spacing: 0.5px; }
  .brand__name .line-sub { display: block; font-size: 12.5px; margin-top: 4px; letter-spacing: 0.2px; }

  .card--front .brand { left: 50px; top: 196px; color: var(--white); }
  .card--front .brand__dot { border: 6px solid var(--white); }
  .card--back .brand { left: 50px; top: 103px; color: var(--brand-blue); }
  .card--back .brand__dot { border: 6px solid var(--brand-blue); }

  .contact {
    position: absolute;
    left: 55px; top: 229px;
    color: var(--brand-blue);
  }
  .contact__name { font-size: 29px; font-weight: 700; line-height: 1.1; }
  .contact__title { font-size: 18px; font-weight: 500; margin-top: 2px; }
  .contact__list { list-style: none; margin-top: 22px; }
  .contact__list li {
    display: flex; align-items: center; gap: 12px;
    font-size: 18px; font-weight: 600;
    height: 27px;
  }
  .contact__icon { width: 22px; height: 22px; flex: none; }
  .contact__icon svg { width: 22px; height: 22px; display: block; }
  .social-dot {
    width: 20px; height: 20px; margin: 1px;
    border-radius: 50%;
    border: 2.5px solid var(--icon-grey);
  }
</style>
</head>
<body>

<section class="card card--front" aria-label="Card front">
  <div class="pattern-area" role="img" aria-label="Faint blueprint background of gears, grids and arrows"></div>
  <div class="emblem-ring"></div>
  <div class="brand">
    <span class="brand__dot"></span>
    <span class="brand__name"><span class="line-main">TALVICK</span><span class="line-sub">INDUSTRIAL MAINTENANCE</span></span>
  </div>
</section>

<section class="card card--back" aria-label="Card back">
  <div class="pattern-area" role="img" aria-label="Faint grey blueprint background of gears and grids"></div>
  <div class="emblem-ring"></div>
  <div class="brand">
    <span class="brand__dot"></span>
    <span class="brand__name"><span class="line-main">TALVICK</span><span class="line-sub">INDUSTRIAL MAINTENANCE</span></span>
  </div>
  <div class="contact">
    <p class="contact__name">Dan Pelfrey Jr.</p>
    <p class="contact__title">Managing Director</p>
    <ul class="contact__list">
      <li>
        <span class="contact__icon"><svg viewBox="0 0 24 24"><path fill="#6e6e6e" d="M6.6 10.8a15.1 15.1 0 0 0 6.6 6.6l2.2-2.2a1 1 0 0 1 1-.25 11.4 11.4 0 0 0 3.6.57 1 1 0 0 1 1 1V20a1 1 0 0 1-1 1A17 17 0 0 1 3 4a1 1 0 0 1 1-1h3.5a1 1 0 0 1 1 1c0 1.25.2 2.45.57 3.57a1 1 0 0 1-.25 1z"/></svg></span>
        <span>555-214-7608</span>
      </li>
      <li>
        <span class="contact__icon"><svg viewBox="0 0 24 24"><rect x="2" y="5" width="20" height="14" fill="#6e6e6e"/><path d="M2 5l10 8 10-8M2 19l7.5-7M22 19l-7.5-7" stroke="#f6f6f6" stroke-width="1.6" fill="none"/></svg></span>
        <span>dan.pelfrey.jr@mailvantor.com</span>
      </li>
      <li>
        <span class="contact__icon"><span class="social-dot" style="display:block"></span></span>
        <span>@talvickindustrial</span>
      </li>
    </ul>
  </div>
</section>

</body>
</html>
```